DJ / Music Prod. studio needs Website.

Web Design needed for a DJ / Music Production Studio. Bright crisp colors, sharp, and user friendly. The design should incorporate the equalizer look that the logo has, however I am not opposed to a different idea if you feel it would look better. When someone gets to the landing page I need them to understand what our services our immediately and be able to easily navigate the content, via both text and the view trail video which will be provided and should be the centerpiece of the landing page. thx good luck!

Target Market(s)

people hosting personal parties and events.

Industry/Entity Type

Party Planning

Logo Text

SpinFreeHost.net

Number of Pages Required

4 page

Font styles to use
Sans Serif

Colors
0592cd
e24096
a54499
6b449b
00a990
000000
86cfc6

Requirements
Must have
• A page where they can submit the info directly on the site. Fill in the blanks type and coinwell button upon submission. A video box linked to our viewtrail account on the main page so the viewtrail videos to play. The 4 pages plus landing page are; 1. Pricing 2. Submit (which is also the pay page) 3 FAQ 4. Contact. Our logo can be the header, and the mirrored one could possibly be the background. I am very open minded and open to creative suggestions. you know what looks best better then I would. Please stay with the same color scheme as the main logo. I will have the full text up within a day or 2. Thx 4 reading and good luck!
Nice to have
• Each pages header the same but in a different color scheme. See zip file
Should not have
• Anything that might take away from it being sharp , clean, and user friendly. This isn't a club dj site but more of a site for everyday people of all demographics who need music for their personal parties and events.

```html
<!DOCTYPE html>
<html lang="en">
<head>
<meta charset="utf-8">
<title>SpinFreeHost.net — DJ / Music Production Studio</title>
<link href="https://fonts.googleapis.com/css2?family=Open+Sans:wght@400;600;700;800&display=swap" rel="stylesheet">
<style>
:root{
  --blue:#0592cd;
  --pink:#e24096;
  --violet:#a54499;
  --purple:#6b449b;
  --teal:#00a990;
  --mint:#86cfc6;
  --black:#000000;
  --page:#141414;
  --panel:#1e1e1e;
  --bar:#2a2a2a;
  --line:#3a3a3a;
  --text:#d8d8d8;
  --muted:#8a8a8a;
  --play:#f26a1b;
}
*{box-sizing:border-box;margin:0;padding:0}
html,body{width:807px;height:1200px;overflow:hidden}
body{background:var(--page);font-family:"Open Sans",Arial,sans-serif;color:var(--text);position:relative}

.site-header{position:absolute;left:0;top:0;width:807px;height:118px;
  background:linear-gradient(90deg,#1a0b24 0%,#3a1350 20%,#0b2a3f 45%,#0d3a33 60%,#3b1030 80%,#1a0b24 100%)}
.equalizer-art{position:absolute;inset:0;
  background:linear-gradient(180deg,rgba(0,0,0,0) 0%,rgba(0,0,0,.55) 100%),
  linear-gradient(90deg,var(--purple),var(--pink),var(--blue),var(--teal),var(--mint),var(--pink),var(--violet));
  opacity:.55}
.brand{position:absolute;left:0;right:0;top:36px;text-align:center;display:flex;justify-content:center;align-items:center;gap:8px}
.brand-mark{width:14px;height:14px;background:var(--pink)}
.brand-name{font-weight:700;font-size:24px;color:#ffffff;letter-spacing:.5px}

.main-nav{position:absolute;left:0;top:118px;width:807px;height:40px;background:#0c0c0c;border-bottom:1px solid var(--line)}
.nav-links{position:absolute;left:82px;top:0;display:flex;list-style:none;height:40px;align-items:center}
.nav-links li{font-size:11px;font-weight:600;color:#bdbdbd;margin-right:40px;letter-spacing:.3px}
.nav-links li.active{color:#fff}
.social{position:absolute;right:82px;top:12px;display:flex;gap:7px}
.social span{width:16px;height:16px;border:1px solid #9a9a9a;border-radius:50%}

.content-panel{position:absolute;left:66px;top:176px;width:676px;height:732px;background:var(--panel);border:1px solid #262626}

.video{position:absolute;left:72px;top:184px;width:664px;height:394px;background:#000;overflow:hidden}
.video-still{position:absolute;inset:0 0 44px 0;
  background:radial-gradient(ellipse at 55% 40%,#b03aa8 0%,#5b2a8a 35%,#1c1040 70%,#0a0614 100%)}
.video-title{position:absolute;left:44px;top:96px;font-size:58px;font-weight:800;line-height:1.05;color:#fff}
.video-play{position:absolute;left:300px;top:130px;width:58px;height:58px;border-radius:50%;background:#fff}
.video-play svg{position:absolute;left:21px;top:17px}
.video-controls{position:absolute;left:0;bottom:0;width:100%;height:44px;background:var(--bar);display:flex;align-items:center;padding-left:12px}
.ctrl-btn{width:26px;height:26px;border-radius:50%;background:var(--play);position:relative}
.ctrl-btn svg{position:absolute;left:9px;top:7px}
.video-name{font-size:12px;color:#cfcfcf;margin-left:14px}
.progress{position:absolute;right:14px;top:21px;width:300px;height:3px;background:#4a4a4a}

.section-bar{position:absolute;left:72px;top:602px;width:664px;height:38px;border-bottom:2px solid var(--violet)}
.section-tab{position:absolute;left:0;top:0;height:38px;width:250px;background:linear-gradient(90deg,var(--purple),var(--violet));
  clip-path:polygon(0 0,92% 0,100% 100%,0 100%);color:#fff;font-size:14px;font-weight:600;padding:9px 12px}
.section-arrows{position:absolute;right:6px;top:14px;display:flex;gap:10px}

.cards{position:absolute;left:80px;top:660px;width:648px;display:flex;gap:24px}
.card{width:200px}
.card-photo{height:122px;border:2px solid #333}
.photo-1{background:linear-gradient(135deg,#3a2a1e,#a07a52 55%,#2a1b12)}
.photo-2{background:linear-gradient(135deg,#2a0d3a,#c2367a 50%,#2b5fa6)}
.photo-3{background:linear-gradient(135deg,#0d1a40,#6b449b 45%,#e24096)}
.card h3{font-size:10px;font-weight:600;color:#cfcfcf;text-align:center;margin-top:12px}
.card p{font-size:9px;line-height:1.5;color:var(--muted);text-align:center;margin-top:6px;padding:0 8px}
.card .more{display:block;text-align:center;font-size:9px;font-weight:700;color:var(--violet);margin-top:8px}

.testimonials-title{position:absolute;left:0;width:807px;top:930px;text-align:center;font-size:20px;font-weight:600;color:#6f6f6f;letter-spacing:1px}
.testimonials-title::after{content:"";display:block;width:140px;height:1px;background:#444;margin:8px auto 0}
.quote{position:absolute;top:990px;width:320px;display:flex;gap:14px}
.quote-1{left:66px}
.quote-2{left:426px}
.avatar{flex:0 0 78px;height:78px;border-radius:50%;border:3px solid #3a3a3a;background:radial-gradient(circle,#c25aa8,#4a2068)}
.quote p{font-size:9px;line-height:1.55;color:var(--muted)}
.quote cite{display:block;font-style:normal;font-size:9px;font-weight:700;color:var(--violet);margin-top:6px}

.site-footer{position:absolute;left:0;top:1128px;width:807px;height:72px;background:#0c0c0c;border-top:1px solid var(--line)}
.footer-col{position:absolute;top:14px}
.footer-col h4{font-size:11px;font-weight:700;color:#cfcfcf;letter-spacing:.5px}
.footer-col p{font-size:8px;color:var(--muted);margin-top:5px}
.col-copy{left:66px}
.col-address{left:260px}
.follow{position:absolute;right:82px;top:22px;display:flex;align-items:center;gap:6px}
.follow h4{font-size:11px;font-weight:700;color:#cfcfcf;margin-right:6px}
.follow span{width:14px;height:14px;background:#cfcfcf;border-radius:2px}
</style>
</head>
<body>

<header class="site-header">
  <div class="equalizer-art" role="img" aria-label="Colourful equalizer bars glowing across the header"></div>
  <div class="brand"><span class="brand-mark"></span><span class="brand-name">SpinFreeHost.net</span></div>
</header>

<nav class="main-nav">
  <ul class="nav-links">
    <li class="active">HOME</li><li>PRICING</li><li>SUBMIT</li><li>FAQ</li><li>CONTACT US</li>
  </ul>
  <div class="social"><span></span><span></span><span></span><span></span></div>
</nav>

<div class="content-panel"></div>

<section class="video">
  <div class="video-still" role="img" aria-label="DJ in a black t-shirt mixing on decks under purple club lights"></div>
  <div class="video-title">WHAT<br>IS<br>SFHN?</div>
  <div class="video-play"><svg width="20" height="24" viewBox="0 0 20 24"><polygon points="0,0 20,12 0,24" fill="#222"/></svg></div>
  <div class="video-controls">
    <div class="ctrl-btn"><svg width="10" height="12" viewBox="0 0 10 12"><polygon points="0,0 10,6 0,12" fill="#fff"/></svg></div>
    <span class="video-name">DJ / Music Production Studio</span>
    <div class="progress"></div>
  </div>
</section>

<div class="section-bar">
  <div class="section-tab">Pros of SFHN Over Hiring a DJ</div>
  <div class="section-arrows">
    <svg width="8" height="10" viewBox="0 0 8 10"><polygon points="8,0 0,5 8,10" fill="#bbb"/></svg>
    <svg width="8" height="10" viewBox="0 0 8 10"><polygon points="0,0 8,5 0,10" fill="#bbb"/></svg>
  </div>
</div>

<div class="cards">
  <article class="card">
    <div class="card-photo photo-1" role="img" aria-label="DJ playing music at a warm-lit party"></div>
    <h3>Your playlist, your party</h3>
    <p>Pick the songs, set the mood and let the mix run all night long.</p>
    <span class="more">READ MORE</span>
  </article>
  <article class="card">
    <div class="card-photo photo-2" role="img" aria-label="Mixing desk lit with pink and blue lights"></div>
    <h3>Honest pricing for everyone</h3>
    <p>Clear prices for every event, from small dinners to big backyard birthday bashes too.</p>
    <span class="more">READ MORE</span>
  </article>
  <article class="card">
    <div class="card-photo photo-3" role="img" aria-label="Guest dancing under colourful stage lights"></div>
    <h3>Book online in minutes</h3>
    <p>Submit your details online, pay securely and get your music ready within two days.</p>
    <span class="more">READ MORE</span>
  </article>
</div>

<h2 class="testimonials-title">TESTIMONIALS</h2>

<blockquote class="quote quote-1">
  <div class="avatar" role="img" aria-label="Portrait of a happy client"></div>
  <div><p>We booked our wedding mix in minutes. The music flowed all evening and every guest asked where we found it. Simple, friendly and great value.</p><cite>Laura M.</cite></div>
</blockquote>
<blockquote class="quote quote-2">
  <div class="avatar" role="img" aria-label="Portrait of a happy client"></div>
  <div><p>Our birthday party sounded like a real club night. Setup was easy and support answered every question fast. We will use it again.</p><cite>Derek P.</cite></div>
</blockquote>

<footer class="site-footer">
  <div class="footer-col col-copy"><h4>COPYRIGHT</h4><p>© 2015 SpinFreeHost.net. All rights reserved.</p></div>
  <div class="footer-col col-address"><h4>ADDRESS</h4><p>2810 Harbor Lane, Glenport, NV 80213</p></div>
  <div class="follow"><h4>FOLLOW US</h4><span></span><span></span><span></span><span></span></div>
</footer>

</body>
</html>
```